Refresh look of our invoices (Excel spreadsheet which converts to PDF) to better match our new look

We have recently updated our Website and other marketing material with a new look and would like to refresh our invoice template so that it better matches our new look.  The template is an excel spreadsheet which we convert to a PDF to send out to our clients.
The main requirement is to incorporate the newer design colours and general look/feel to align with what is on our website www.corvalhill.com.au
It is extremely important that excel formula functionality and general layout are much the same although we are open to any design suggestions you might have.
Please note:
-Totals figures and news panel must remain on the first page
-We need full ability to edit embedded formulas and Excel spreadsheet is NOT to be password protected as we will only be using it internally.
-It is crucial that the second and subsequent pages can be extended (duplicated) internally to allow for larger multi page entries. Some of our clients invoices run up to 4/5 pages in length and we need the abilty to keep adding rows)
-possibility to add a "convert to PDF" button within the sheet which provides a 1 click solution to convert to PDF rather than the manual 2 step process to convert.... If that can be done, we would not want the "convert to PDF" button to show on final PDF converted version we issue to our customers.   Ideally, a single "convert to PDF and print first cover page only" in 1 single click button named 'convert to PDF & print' would be really handy.  -  (Just to explain why - we email out a PDF version of invoice to our clients and only print off first page with totals for our records)
The design for the first page can be different from the second & subsequent pages (eg first page can be more fancy with following pages more basic)

Finance Industry
Marketing

```html
<!DOCTYPE html>
<html lang="en">
<head>
<meta charset="utf-8">
<title>Corval Hill – Recipient Created Tax Invoice</title>
<link href="https://fonts.googleapis.com/css2?family=Arimo:wght@400;700&display=swap" rel="stylesheet">
<style>
:root{
  --bg:#e9e7e3;
  --paper:#ffffff;
  --ink:#333333;
  --grey:#6d6e70;
  --green:#76923c;
  --red:#e01f1f;
  --rule:#3a3a3a;
}
*{box-sizing:border-box;margin:0;padding:0}
html,body{width:961px;height:1200px;overflow:hidden;background:var(--bg)}
body{position:relative;font-family:"Arimo",Arial,sans-serif;color:var(--ink)}
.page{position:absolute;left:72px;width:823px;background:var(--paper);box-shadow:0 1px 4px rgba(0,0,0,.25)}
.page--cover{top:12px;height:582px}
.page--detail{top:602px;height:586px;border-top:3px solid #222}
.abs{position:absolute}
.brand{left:48px;top:50px;display:flex;align-items:center;gap:10px}
.brand__mark{width:30px;height:30px;background:var(--grey)}
.brand__name{font-size:44px;font-weight:700;color:var(--grey);letter-spacing:1px;line-height:1}
.company{right:113px;top:55px;text-align:right;font-size:10px;font-weight:700;line-height:12.5px;color:#222}
.company__web{color:var(--green)}
.header-rule{left:48px;top:103px;width:662px;height:3px;background:var(--rule)}
.abn{right:113px;top:118px;font-size:10px;font-weight:700}
.doc-title{left:0;width:756px;top:130px;text-align:center;font-size:13px;font-weight:700;color:#444}
.invoice-date{left:548px;top:153px;font-size:10px;font-weight:700;color:#444}
.referrer{left:48px;font-size:9.5px;font-weight:700;color:#444;line-height:17px}
.totals{right:113px;top:256px;font-size:12px;font-weight:700;color:#444}
.totals__row{display:flex;justify-content:flex-end;line-height:14px}
.totals__label{text-align:right}
.totals__value{width:92px;text-align:right}
.totals__value--neg{color:var(--red)}
.totals__grand{display:flex;justify-content:flex-end;align-items:center;margin-top:4px}
.totals__grand .totals__label{border-bottom:1.5px solid #333;padding:0 8px 1px 0;margin-right:6px}
.totals__grand .totals__value{border:1.5px solid #333;padding:1px 3px;width:93px}
.news{left:48px;top:432px;width:662px;font-size:10px;font-weight:700;line-height:13px;color:#333}
.news__title{color:var(--red)}
.news__link{color:var(--green)}
.privacy{left:48px;top:487px;width:662px;border:1px solid #333;font-size:7.5px;font-style:italic;line-height:9px;padding:1px 3px}
.address{left:84px;top:516px;font-size:10px;font-weight:700}
.detail-name{left:48px;top:68px;font-size:9.5px;font-weight:700;color:#444}
table.ledger{position:absolute;left:44px;top:122px;width:667px;border-collapse:collapse;table-layout:fixed;font-size:9.5px;color:#444}
.ledger th{background:var(--green);color:#fff;font-weight:700;height:17px;padding:0 3px;text-align:right}
.ledger td{height:12px;line-height:12px;padding:0 3px;text-align:right}
.ledger .l{text-align:left}
.ledger tr.gap td{height:9px}
.fees{position:absolute;left:44px;top:352px;width:667px;border-collapse:collapse;table-layout:fixed;font-size:9px;color:var(--red)}
.fees td{height:12px;padding:0 3px;text-align:right}
.fees td.l{text-align:left}
.fees b{text-decoration:underline}
.fees u{text-decoration:underline}
.summary{position:absolute;left:44px;top:385px;width:667px;border-collapse:collapse;table-layout:fixed;font-size:12px;font-weight:700;color:#444}
.summary th{background:var(--green);color:#fff;font-size:9.5px;height:15px;padding:0 3px;text-align:right}
.summary td{height:26px;padding:0 3px;text-align:right;border-bottom:2px solid #444}
.summary .neg{color:var(--red)}
.summary .boxed span{border:1.5px solid #333;padding:1px 3px}
</style>
</head>
<body>

<section class="page page--cover">
  <div class="abs brand"><span class="brand__mark"></span><span class="brand__name">CORVAL HILL</span></div>
  <div class="abs company">
    Corval Hill Pty Ltd<br>Ph (1300) 415 268<br>Fax (1300) 415 279<br>
    <span class="company__web">www.corvalhill.com.au</span>
  </div>
  <div class="abs header-rule"></div>
  <div class="abs abn">ABN&nbsp; 71 402 336 918</div>
  <h1 class="abs doc-title">RECIPIENT CREATED TAX INVOICE</h1>
  <div class="abs invoice-date">Invoice Date:&nbsp; 13-Sep-13</div>

  <div class="abs referrer" style="top:172px">Referrer name</div>
  <div class="abs referrer" style="top:189px">referrer address line 1<br>referrer address line 2</div>
  <div class="abs referrer" style="top:233px">ABN: 00 000 000 000</div>

  <div class="abs totals">
    <div class="totals__row"><span class="totals__label">Upfront</span><span class="totals__value">$3,000.00</span></div>
    <div class="totals__row"><span class="totals__label">Trail</span><span class="totals__value">$202.26</span></div>
    <div class="totals__row"><span class="totals__label">Adjustments</span><span class="totals__value totals__value--neg">-$50.00</span></div>
    <div class="totals__row"><span class="totals__label">GST</span><span class="totals__value">$315.24</span></div>
    <div class="totals__grand"><span class="totals__label">TOTAL AMOUNT DEPOSITED</span><span class="totals__value">$3,467.50</span></div>
  </div>

  <div class="abs news">
    <div class="news__title">* CORVAL CONNECT - Referral management software *</div>
    The Corval Connect software provides you with a fully compliant referral process that is supported by the lenders. Apart from making new referrals, you can also read lender updates on deal progress and lodge enquires for outstanding commission payments. You can login by going to the dedicated Corval Connect website at: <span class="news__link">www.corvalmembers.com.au</span>
  </div>
  <div class="abs privacy">This report contains confidential client information. Disclosure of customer information such as loan details and lenders to third parties may be a contravention of the Privacy Act, unless they are authorised to receive such details.</div>
  <div class="abs address">Corval Hill Pty Ltd&nbsp; Level 12, 88 Harlow Street Melbourne Vic 3000</div>
</section>

<section class="page page--detail">
  <div class="abs detail-name">referrer name</div>

  <table class="ledger">
    <colgroup><col style="width:114px"><col style="width:74px"><col style="width:58px"><col style="width:80px"><col style="width:77px"><col style="width:48px"><col style="width:46px"><col style="width:84px"><col style="width:86px"></colgroup>
    <thead><tr><th class="l">Client</th><th class="l">Lender</th><th class="l">Loan</th><th>Amount</th><th>Upfront</th><th>Trail</th><th>Adj.</th><th>GST</th><th>TOTAL</th></tr></thead>
    <tbody>
      <tr class="gap"><td colspan="9"></td></tr>
      <tr><td class="l">dsgfg</td><td class="l">Harbourline</td><td></td><td>$34,182.00</td><td>$0.00</td><td>$3.48</td><td>$0.00</td><td>$0.35</td><td>$3.83</td></tr>
      <tr><td class="l">ggffgfd</td><td class="l">Harbourline</td><td></td><td>$132,583.00</td><td>$0.00</td><td>$13.51</td><td>$0.00</td><td>$1.35</td><td>$14.86</td></tr>
      <tr><td class="l">fggfdfg</td><td class="l">Harbourline</td><td></td><td>$119,988.00</td><td>$0.00</td><td>$12.23</td><td>$0.00</td><td>$1.22</td><td>$13.45</td></tr>
      <tr><td class="l">gfdfg</td><td class="l">Harbourline</td><td></td><td>$479,999.00</td><td>$0.00</td><td>$48.92</td><td>$0.00</td><td>$4.89</td><td>$53.81</td></tr>
      <tr><td class="l">dfg</td><td class="l">Harbourline</td><td></td><td>$134,161.00</td><td>$0.00</td><td>$13.67</td><td>$0.00</td><td>$1.37</td><td>$15.04</td></tr>
      <tr><td class="l">gdfg</td><td class="l">Harbourline</td><td></td><td>$78,927.00</td><td>$0.00</td><td>$8.05</td><td>$0.00</td><td>$0.81</td><td>$8.86</td></tr>
      <tr><td class="l">dffdgvfgf</td><td class="l">Harbourline</td><td></td><td>$149,400.00</td><td>$0.00</td><td>$15.22</td><td>$0.00</td><td>$1.52</td><td>$16.74</td></tr>
      <tr><td class="l">fgdg</td><td class="l">Harbourline</td><td></td><td>$99,805.00</td><td>$0.00</td><td>$10.17</td><td>$0.00</td><td>$1.02</td><td>$11.19</td></tr>
      <tr><td class="l">ffgdggf</td><td class="l">Harbourline</td><td></td><td>$377,100.00</td><td>$0.00</td><td>$38.43</td><td>$0.00</td><td>$3.84</td><td>$42.27</td></tr>
      <tr><td class="l">df</td><td class="l">Harbourline</td><td></td><td>$101,738.00</td><td>$0.00</td><td>$10.37</td><td>$0.00</td><td>$1.04</td><td>$11.41</td></tr>
      <tr><td class="l">gdgsdgsdf</td><td class="l">Harbourline</td><td></td><td>$50,564.00</td><td>$0.00</td><td>$5.15</td><td>$0.00</td><td>$0.52</td><td>$5.67</td></tr>
      <tr><td class="l">dsfggddfg</td><td class="l">Harbourline</td><td></td><td>$108,500.00</td><td>$0.00</td><td>$7.38</td><td>$0.00</td><td>$0.74</td><td>$8.12</td></tr>
      <tr><td class="l">dfdfgdsfghfd</td><td class="l">Harbourline</td><td></td><td>$230,807.00</td><td>$0.00</td><td>$15.68</td><td>$0.00</td><td>$1.57</td><td>$17.25</td></tr>
      <tr><td class="l">dfdjsf</td><td class="l">Southgate Bank</td><td></td><td>$600,000.00</td><td>$3,000.00</td><td>$0.00</td><td>$0.00</td><td>$300.00</td><td>$3,300.00</td></tr>
    </tbody>
  </table>

  <table class="fees">
    <colgroup><col style="width:451px"><col style="width:90px"><col style="width:84px"><col style="width:42px"></colgroup>
    <tr><td class="l"><b>Software Fee</b> of $50 (+GST) - only applies in months with a new settlement occurring</td><td>-$50.00</td><td>-$5.00</td><td>-$55.00</td></tr>
    <tr><td class="l"><b>Admin Fee</b> of $50 (+GST) - deducted from trail if <u>no new deals within last 6 months</u></td><td>$0.00</td><td>$0.00</td><td>$0.00</td></tr>
  </table>

  <table class="summary">
    <colgroup><col style="width:246px"><col style="width:80px"><col style="width:77px"><col style="width:48px"><col style="width:46px"><col style="width:84px"><col style="width:86px"></colgroup>
    <thead><tr><th></th><th>Loan Book</th><th>Upfront</th><th>Trail</th><th>Adj.</th><th>GST</th><th>TOTAL</th></tr></thead>
    <tbody><tr><td></td><td>$2,697,754.00</td><td>$3,000.00</td><td>$202.26</td><td class="neg">-$50.00</td><td>$315.24</td><td class="boxed"><span>$3,467.50</span></td></tr></tbody>
  </table>
</section>

</body>
</html>
```